Sassy Funky Web Design Project

NOTE: PAYMENT IS GUARANTEED for this project :)

++++++++++++++++++

I meant to share with you my mission for Caring Summit:

To inspire nurses to take action that impacts change in their lives, their organizations, or even the world.

Values:
I – Integrity
M – Mentoring / Motivation
P – Passion for excellence
A – Accountability
C – Competence / knowledge/ achievement
T – Transformation – positive change

++++++++++++++++++

This is a Membership site so will need to show 'Members Login' etc.

Please make sure you use SUPER HIGH QUALITY PHOTOGRAPHY / IMAGES :)

This is a WORDPRESS site for my client - here's some questions I asked her with her answers:

1. Why do you want a website (or have your current site redesigned)?

I want a website to generate income, and residual income, promote quality education material to professionals that is not the same on-line programs point and click to answer questions. I want an interactive way to make a impact in nursing hence CaringSUMMIT.

2. What’s your business/organization all about?

My parent company is Verity Brook Partners, LLC. I started it in 2001 and I provide consultative services to the legal and medical professionals. Mostly legal professionals; attorneys, and offer expert witness testimony. I also present full-day seminars regarding legal aspects of healthcare for nurses and hospital executive leaders. I am always promoting the professionalism in nursing where ever I can.

3. What sets your business apart from your competition?

What I will offer is instant access to quality and reliable clinical information and reliable business support for legal nurse consultants. I have not found another website that offers videos of clinical skills that nurses can watch over and over again without paying a lot of money for. Most of the information for nurses is through online learning read a packet, answer questions, and hopefully, maybe, they learned something. One of the reasons why my seminars are so well attended is they are interactive, and I use real examples to act out scenarios. I want nurses to be able to access short 7-10 minute video/podcasts that will show them how things are done and not just reading about it. Assessment skills will be performed on my family members in a clinic setting to create a realistic view. I want these to be somehow interactive if possible to reinforce the learning. Maybe you have some ideas on that.

For the legal nurse consultants. The programs are driving the “certification” outcome. When the nurses complete these programs, they have no experience and therefore are not able to recover their investment. I want to provide for them the same type of visual education support as the clinical nurses. These two audiences do not have to be mutually exclusive because they do tend to overlap in the real world.

I provide personal mentoring for novice legal nurse consultants in one week programs to support the application need in the LNC community. These weeks are valuable to the novice LNC trying to get started.

4. What problems does your business solve?

Application of concepts which is where I came up with Verity Brook Partners. I also have a tag with CaringSUMMIT I have used: Education, training, application. I put the theory into practice. I translate the pages to the living people.

5. Who are your prospective customers or visitors?

Customers:
Nurses, Advanced Practice Nurses, Legal Nurse Consultants, Attorneys for the clinical/medical information, Universities that offer nursing programs,
Nursing students (I really want to pursue this niche, perhaps a discount for enrolled students???)

Visitors:
Hospital Chief Nursing Officers, Attorneys, Long Term Care Administrators, Faculty of Nursing programs.

6. What do you NOT want on your website?

A flat appearing, boxy, traditional site. I want the nurses to be able to navigate through without much effort, remember many are technologically challenged….
NOooo cartoons… not too many stock photos, I would rather take real images if at all possible to keep the site “alive and real”.

What do you like?

QRV.tv: the listing of videos is going to be important in my site because I will be making clinical example videos and interview videos that can be viewed over and over again by the Platinum members. I plan to have a blog and many downloads available as well.

Tovamesh.com: I like the layout but I do want more interaction with mine. I do like the are you a training leader? Department leader: emerging leader? Componenets because I am addressing Nurses, Nurse Leaders, Legal Nurse Consultants… this would be important to establish right up front. I particularly like the video enhanced special report the new prospect has access to. I will do this for my site. I think it is also cool that you can change the color of the landing page to your liking.

www.thebrindlecove.com: I like a lot of things on this website but it is a bit difficult to navigate for even me. I like the short one minute capture of audio cds. I do plan to have CD material available. I do like the what you get with each level of membership under brindlelink tab. Some of the pages are not easy to read because the color is too dark and the font color is not contrasted enough. I like the tips in ten downloads on CD as well. I can see this working with mine as similar formatting with of course difference content.

www.ginaforsby.org: I do like the section she has on photo gallery where I can post event that have taken place as I speak, and work one-on-one with nurses across the country. (not the fashion shoot ?).

www.7horizons.com: I love the rollover interaction, the eyes constantly moving to the movement across the site.
http://www.dorvesta.org/DorvestaMultimedia.aspx?VideoId=8830461729004&type=M Quick lane video using sketchpad is a cool idea.

www.pebblevault.com - nice and clean

11. Please give us a list of websites that you DON’T Like and Why you Don’t like them.

www.lurn.com: landing page is way too crowded, too many colors, I don’t know where to go for what I would be looking for. Font is too small with large amounts of content.

www.casewardhub.com: this site is way too busy and difficult to navigate however I do like the page titled: Memorable BRWP cases. I would use a page like this for memorable Caring Summit experiences that would encourage others and remember the great things nurses do.

www.wardskills.com: Do not like at all. Way to juvenile.

Colour Scheme:

The colors palette I like is…. I think you will get the general idea of the color scheme. I like the yellow on dark colors so it pops, make sense?

F7C40E
4819A9
2E1FAC
F7D80E
Updates

Payment is guaranteed for this project now! :)

Thank you

Target Market(s)

Customers: Nurses, Advanced Practice Nurses, Legal Nurse Consultants, Attorneys for the clinical/medical information, Universities that offer nursing

Values:
I – Integrity
A – Accountability

Industry/Entity Type

Healthcare

Requirements
Must have
• professional, clean, VERY HIGH QUALITY IMAGES/ PHOTOGRAPHY e.g. PixQuarry
Nice to have
• Brock:
I have shown the design template to several people to get their first impression. I was shocked. They thought of the Tacoma Riveters! The football team. Ouch. I don’t want that. Crazy what others see.
Can we please change the color scheme to incorporate the colors below with the same layout. The Layout is good, it is the color I need to work a bit more on. Sorry about this but I don’t want to be a Riveters fan.

336699
FFCC66
FFFFFF
003366

Yvonne

New logo required: Caring Summit - DO NOT USE MEDICAL
Should not have
• childish graphics, or icons.
Don't want to see unprofessional site with clumsy type or template type designs. We can include some photos.

```html
<!DOCTYPE html>
<html lang="en">
<head>
<meta charset="utf-8">
<title>Caring Summit</title>
<link href="https://fonts.googleapis.com/css2?family=Ubuntu:wght@300;400;500&display=swap" rel="stylesheet">
<style>
:root{
  --orange:#f39200;
  --orange-top:#fbc21f;
  --orange-bottom:#f7931e;
  --ink:#333333;
  --hero-ink:#3b2a10;
  --panel:#e9e9e9;
  --white:#ffffff;
}
*{box-sizing:border-box;margin:0;padding:0}
html,body{width:819px;height:1200px;overflow:hidden;background:var(--white)}
body{font-family:"Ubuntu",sans-serif;color:var(--ink);position:relative}
.abs{position:absolute}
.top-strip{left:0;top:0;width:819px;height:8px;background:linear-gradient(var(--orange-top),var(--orange-bottom))}
.top-rule{left:118px;top:37px;width:584px;height:1px;background:#e5e5e5}
.social{left:543px;top:20px;display:flex;gap:6px}
.social span{width:11px;height:11px;border-radius:2px;background:#9aa5b3}
.brand{left:128px;top:42px;font-size:25px;font-weight:400;letter-spacing:1px;color:var(--orange);text-transform:uppercase}
.search{left:482px;top:82px;width:207px;height:21px;border:2px solid #dcdcdc;border-radius:3px;background:#fff;display:flex;align-items:center;font-size:7px}
.search .field{flex:1;color:#aaa;font-style:italic;padding-left:5px;display:flex;align-items:center;gap:4px}
.search .btn{width:36px;border-left:1px solid #ddd;height:100%;display:flex;align-items:center;justify-content:center;color:#555}
.band{left:0;width:819px;background:linear-gradient(var(--orange-top),var(--orange-bottom))}
.hero-band{top:128px;height:218px}
.nav{left:130px;top:116px;width:560px;height:28px;background:linear-gradient(#fff,#eeeeee);border:1px solid #d5d5d5;display:flex;font-size:7.5px;font-weight:500;color:#444}
.nav span{display:flex;align-items:center;justify-content:center;border-right:1px solid #d5d5d5;white-space:nowrap}
.nav span:last-child{border-right:0}
.hero-img{left:158px;top:169px;width:264px;height:166px;border:2px solid #fff;background:linear-gradient(120deg,#8fb7d9,#e9e2da 55%,#c7a88c)}
.hero-title{left:446px;top:172px;font-size:12px;font-weight:400;color:var(--hero-ink)}
.hero-text{left:446px;top:197px;width:220px;font-size:7.6px;line-height:11.7px;color:var(--hero-ink)}
.btn-more{background:#fff;border:1px solid #d8d8d8;font-size:7.5px;color:#444;display:flex;align-items:center;justify-content:center}
.dots{left:396px;top:341px;display:flex;gap:2px}
.dots span{width:7px;height:7px;border-radius:50%;background:#555;border:1px solid #fff}
.dots span:first-child{background:var(--orange)}
.sidebar{left:122px;top:362px;width:111px;height:190px;border:1px solid #cfcfcf;padding:2px 0 0 8px;font-size:7.3px;line-height:11.7px}
.content{left:241px;top:361px;width:280px;font-size:7.5px;line-height:12.8px}
.content h2,.section-title{font-weight:300;color:var(--orange)}
.content h2{font-size:11px;margin-bottom:4px}
.content-2{left:241px;top:480px;width:432px;font-size:7.5px;line-height:12.8px}
.content-2 h3{font-size:7.8px;font-weight:500}
.login{left:534px;top:366px;width:164px;height:108px;background:var(--panel);border-radius:4px}
.login-tab{left:580px;top:362px;width:74px;height:25px;background:var(--orange);border:2px solid #fff;border-top:0;border-radius:0 0 4px 4px;color:#222;font-size:7.5px;display:flex;align-items:center;justify-content:center;gap:3px;box-shadow:0 1px 2px rgba(0,0,0,.25)}
.input{left:552px;width:132px;height:18px;background:#fff;border:1px solid #dedede;border-radius:3px;font-size:7px;padding-left:5px;display:flex;align-items:center}
.remember{left:552px;top:454px;font-size:6.8px;display:flex;align-items:center;gap:3px}
.remember i{width:5px;height:5px;border-radius:50%;background:var(--orange)}
.signin{left:632px;top:450px;width:52px;height:16px;background:var(--orange);border-radius:8px;font-size:7px;display:flex;align-items:center;justify-content:center}
.section-title{font-size:14px}
.video-title{left:122px;top:570px}
.video-rule{left:118px;top:592px;width:584px;height:1px;background:linear-gradient(90deg,transparent,#e0a040,transparent)}
.main-band{top:594px;height:588px}
.video{top:609px;width:170px;height:110px;border:2px solid #fff;background:linear-gradient(110deg,#dfe7ee,#b8c9d9 60%,#f1f1f1)}
.video .play{position:absolute;left:72px;top:31px;width:28px;height:26px;background:var(--orange);display:flex;align-items:center;justify-content:center}
.video .cap{position:absolute;left:0;right:0;bottom:0;height:28px;background:rgba(70,70,70,.55);color:#fff;font-size:7.3px;line-height:10px;padding:4px 0 0 4px}
.treat{left:122px;top:730px;width:568px;height:163px;background:#fff;border-radius:3px}
.treat-title{left:134px;top:736px}
.col{top:766px;font-size:7.3px;line-height:11.7px}
.card{background:#fff;border-radius:3px}
.card h4{position:absolute;left:10px;top:9px;font-size:10.5px;font-weight:300;color:#333;text-transform:uppercase;white-space:nowrap}
.card .ph{position:absolute;top:29px;width:121px;height:86px}
.card p{position:absolute;top:37px;width:68px;font-size:9.4px;font-weight:300;line-height:12.8px}
.card .btn-more{position:absolute;width:58px;height:14px}
.card.feat h4{left:7px;top:5px;font-size:11px;font-weight:400;text-transform:none}
.feat .sub{position:absolute;left:7px;top:20px;font-size:7.5px;color:#555;white-space:nowrap}
.thumbs{left:567px;top:1047px;display:grid;grid-template-columns:repeat(3,38px);gap:2px}
.thumbs span{height:38px;background:linear-gradient(135deg,#f0c7b4,#d9a48f)}
.see{left:567px;top:1156px;width:61px;height:8px;background:var(--orange);font-size:5px;color:#222;display:flex;align-items:center;justify-content:center}
.footer{left:0;top:1189px;width:819px;text-align:center;font-size:6.4px;color:#444}
</style>
</head>
<body>
<div class="abs top-strip"></div>
<div class="abs top-rule"></div>
<div class="abs social" aria-label="Social links"><span></span><span></span><span></span><span></span></div>
<div class="abs brand">Caring Summit</div>
<div class="abs search">
  <div class="field"><svg width="7" height="7" viewBox="0 0 10 10"><circle cx="4" cy="4" r="3" fill="none" stroke="#555" stroke-width="1.5"/><line x1="6.3" y1="6.3" x2="9.5" y2="9.5" stroke="#555" stroke-width="1.5"/></svg>Search on Caring Summit</div>
  <div class="btn">Search</div>
</div>

<div class="abs band hero-band"></div>
<nav class="abs nav">
  <span style="width:44px">Home</span><span style="width:58px">Videos</span><span style="width:58px">Seminars</span><span style="width:56px">Mentoring</span><span style="width:62px">Downloads</span><span style="width:58px">Our Blog</span><span style="width:58px">About us</span><span style="width:54px">Contact</span><span style="flex:1">Members Area</span>
</nav>
<div class="abs hero-img" role="img" aria-label="Nurse educator demonstrating a patient assessment in a clinic"></div>
<h1 class="abs hero-title">Clinical Skills Library</h1>
<p class="abs hero-text">Short 7-10 minute videos show nurses how clinical skills are really done, not just how to read about them. Every assessment is performed on real people in a clinic setting, so the view stays realistic. Platinum members can watch each skill again and again, answer quick questions that reinforce the learning, and download notes to take to their next shift on the unit...</p>
<div class="abs btn-more" style="left:608px;top:296px;width:58px;height:14px">read more..</div>
<div class="abs dots"><span></span><span></span><span></span></div>

<aside class="abs sidebar">Clinical Skills<br>Assessment Videos<br>Patient Safety<br>Legal Nurse<br>Consulting<br>Expert Witness Prep<br>Memorable Cases<br>Mentoring Weeks<br>Nurse Leadership<br>Seminars &amp; Events<br>Podcasts<br>CD Library<br>Tips in Ten<br>Downloads<br>Member FAQ</aside>

<section class="abs content">
  <h2>Education</h2>
  <p>How do nurses learn best? By watching and doing.<br>Caring Summit puts the theory into practice.<br>Clinical Videos<br>Our assessment videos are filmed in a real clinic. Nurses see each step performed, then check what they learned with short interactive questions instead of a packet to read.</p>
</section>
<section class="abs content-2">
  <h3>Legal Nurse Consultants</h3>
  <p>Certification alone does not build experience. Our one week mentoring programs and visual case studies help novice legal nurse consultants apply what they learned, win their first clients and recover their investment. Attorneys, nursing faculty and nurse leaders will find reliable clinical information and business support here too.</p>
</section>

<div class="abs login"></div>
<div class="abs login-tab"><svg width="8" height="9" viewBox="0 0 8 9"><path d="M2 4V2.5a2 2 0 0 1 4 0V4" fill="none" stroke="#222" stroke-width="1.2"/><rect x="0.5" y="4" width="7" height="5" rx="1" fill="#222"/></svg>Members Login</div>
<div class="abs input" style="top:400px">Username</div>
<div class="abs input" style="top:426px">*********</div>
<div class="abs remember"><i></i>Remember Me</div>
<div class="abs signin">Sign-in</div>

<h2 class="abs section-title video-title">Videos that help you grow in your profession</h2>
<div class="abs video-rule"></div>
<div class="abs band main-band"></div>

<div class="abs video" style="left:132px" role="img" aria-label="Nurse performing a patient assessment"><div class="play"><svg width="8" height="10"><path d="M0 0L8 5L0 10Z" fill="#fff"/></svg></div><div class="cap">how to perform a focused patient<br>assessment in the clinic ?</div></div>
<div class="abs video" style="left:324px" role="img" aria-label="Nurse reviewing a patient chart"><div class="play"><svg width="8" height="10"><path d="M0 0L8 5L0 10Z" fill="#fff"/></svg></div><div class="cap">what does an attorney look for<br>in a nursing chart review ?</div></div>
<div class="abs video" style="left:517px" role="img" aria-label="Nurse leader speaking with staff"><div class="play"><svg width="8" height="10"><path d="M0 0L8 5L0 10Z" fill="#fff"/></svg></div><div class="cap">how can nurse leaders build<br>accountability on the unit ?</div></div>

<div class="abs treat"></div>
<h2 class="abs section-title treat-title">Resources for every nursing role :</h2>
<div class="abs col" style="left:136px">Clinical Skills Videos<br>Assessment Checklists<br>Patient Safety<br>Medication Review<br>Wound Care Basics<br>Vital Signs Refresher<br>Charting Tips<br>Fall Prevention<br>Pain Assessment<br>Shift Handoff</div>
<div class="abs col" style="left:250px">Advanced Assessment<br>Diagnostic Reasoning<br>Case Presentations<br>Prescribing Safety<br>Care Plans<br>Clinical Podcasts<br>Practice Updates<br>Peer Interviews<br>Journal Club<br>Evidence Summaries</div>
<div class="abs col" style="left:364px">Mentoring Weeks<br>Memorable Cases<br>Chart Review Skills<br>Report Writing<br>Expert Witness Prep<br>Deposition Basics<br>Business Support<br>Marketing to Firms<br>Tips in Ten<br>CD Library</div>
<div class="abs col" style="left:484px">Leadership Seminars<br>Legal Aspects of Care<br>Risk Management<br>Staff Development<br>Accountability<br>Policy Review<br>Emerging Leaders<br>Department Leaders<br>Training Leaders<br>Event Gallery</div>
<div class="abs col" style="left:592px">Student Discount<br>Skills Lab Videos<br>Exam Preparation<br>Clinical Rotations<br>Care Plan Help<br>Study Podcasts<br>Career Paths<br>Faculty Resources<br>First Job Tips<br>Nurse Mentors</div>

<article class="abs card" style="left:122px;top:904px;width:212px;height:128px">
  <h4>Watch clinical skills</h4>
  <div class="ph" style="left:9px;background:linear-gradient(135deg,#d9e3ec,#9fb6c9)" role="img" aria-label="Nurse checking a patient's blood pressure"></div>
  <p style="left:141px">See how real assessments are done, step by step!</p>
  <div class="btn-more" style="left:141px;top:100px">read more..</div>
</article>
<article class="abs card" style="left:342px;top:904px;width:211px;height:128px">
  <h4>Legal nurse mentoring</h4>
  <div class="ph" style="left:10px;background:linear-gradient(135deg,#e6ddd0,#b79e82)" role="img" aria-label="Mentor and legal nurse consultant reviewing case files"></div>
  <p style="left:142px">One week programs put theory into practice.</p>
  <div class="btn-more" style="left:142px;top:100px">read more..</div>
</article>
<article class="abs card feat" style="left:560px;top:904px;width:138px;height:115px">
  <h4>Featured Video</h4>
  <div class="sub">Inside the clinic: assessment</div>
  <div style="position:absolute;left:19px;top:34px;width:91px;height:66px;background:linear-gradient(135deg,#dde6ee,#a9bccd)" role="img" aria-label="Video still of a clinic assessment"></div>
  <svg style="position:absolute;left:56px;top:58px" width="18" height="18"><circle cx="9" cy="9" r="8" fill="rgba(255,255,255,.6)"/><path d="M7 5L13 9L7 13Z" fill="#fff"/></svg>
</article>

<article class="abs card" style="left:122px;top:1040px;width:212px;height:130px">
  <h4>Seminars for nurse leaders</h4>
  <div class="ph" style="left:9px;background:linear-gradient(135deg,#c9cfd8,#e7ddd3 60%,#a8a49f)" role="img" aria-label="Nurse leaders at an interactive seminar"></div>
  <p style="left:141px">Interactive days with real scenarios acted out live.</p>
  <div class="btn-more" style="left:141px;top:101px">read more..</div>
</article>
<article class="abs card" style="left:342px;top:1040px;width:211px;height:130px">
  <h4>Membership for students</h4>
  <div class="ph" style="left:10px;background:linear-gradient(135deg,#f0d7c0,#c88d6a)" role="img" aria-label="Nursing students studying together"></div>
  <p style="left:142px">Enrolled nursing students save on every level!</p>
  <div class="btn-more" style="left:142px;top:101px">read more..</div>
</article>
<article class="abs card feat" style="left:560px;top:1027px;width:138px;height:143px">
  <h4 style="font-size:11.5px">Follow Us</h4>
</article>
<div class="abs thumbs" role="img" aria-label="Gallery of seminar and event photos"><span></span><span></span><span></span><span></span><span></span><span></span></div>
<div class="abs see">See event photos</div>

<footer class="abs footer">© Copyright 2012 Caring Summit - All rights reserved - Imprint - Sitemap - TOP</footer>
</body>
</html>
```